Business Card Design Project

We are an agricultural business based in Brisbane.
We design, manage and operate regional saleyards. Our logo is green/silver in colour and details of our business can be found on our website www.vodemarketyards.com.au

Just wanting a corporate design for some business cards and include name, position, contact details.

Thanks

Industry/Entity Type

Business

```html
<!DOCTYPE html>
<html lang="en">
<head>
<meta charset="utf-8">
<title>Vode Market Yards – Business Card</title>
<link href="https://fonts.googleapis.com/css2?family=Arimo:wght@400;700&display=swap" rel="stylesheet">
<style>
  :root {
    --board: #dedede;
    --label: #4a4a4a;
    --green: #2a8a3e;
    --ink: #1f1f1f;
    --card: #ffffff;
    --sky-top: #9cc3e6;
    --sky-low: #dbe9f3;
    --field-high: #c9b57a;
    --field-low: #b59a55;
    --band: #c6e2cd;
    --faint: rgba(0,0,0,0.028);
    --rule: #c8c8c8;
  }
  * { box-sizing: border-box; margin: 0; padding: 0; }
  html, body { width: 1200px; height: 780px; overflow: hidden; }
  body {
    background: var(--board);
    font-family: "Arimo", Arial, sans-serif;
    position: relative;
    color: var(--ink);
  }
  .side-label {
    position: absolute;
    font-weight: 700;
    font-size: 36px;
    line-height: 40px;
    color: var(--label);
  }
  .side-label.front { left: 614px; top: 94px; }
  .side-label.back { left: 538px; top: 386px; }

  .card {
    position: absolute;
    width: 540px;
    height: 330px;
    border-radius: 28px;
    overflow: hidden;
    background: var(--card);
    box-shadow: 0 4px 8px rgba(0,0,0,0.25);
  }
  .card.front { left: 34px; top: 22px; }
  .card.back-field { left: 34px; top: 436px; }
  .card.back-plain { left: 620px; top: 436px; }

  .landscape {
    position: absolute; inset: 0;
    background: linear-gradient(180deg, var(--sky-top) 0%, var(--sky-low) 55%, var(--field-high) 60%, var(--field-low) 100%);
  }
  .brand-name {
    position: absolute;
    left: 30px; width: 354px; top: 54px;
    text-align: center;
    font-weight: 700;
    font-size: 38px;
    line-height: 42px;
    letter-spacing: 1px;
    color: var(--ink);
    white-space: nowrap;
  }

  .faded-landscape {
    position: absolute; left: 0; right: 0; bottom: 0; height: 150px;
    background: linear-gradient(180deg, rgba(255,255,255,1) 0%, rgba(226,214,178,0.7) 45%, var(--field-high) 100%);
  }
  .faint-name {
    position: absolute;
    font-weight: 700;
    font-size: 78px;
    line-height: 90px;
    color: var(--faint);
    white-space: nowrap;
  }
  .back-field .faint-name { left: 296px; top: 30px; }
  .back-plain .faint-name { left: 280px; top: 62px; }

  .person { position: absolute; }
  .name { font-weight: 700; font-size: 22px; color: var(--green); line-height: 26px; }
  .role { font-weight: 700; font-size: 16px; line-height: 20px; color: var(--ink); }
  .contacts { font-size: 15.5px; line-height: 20px; margin-top: 21px; }
  .contacts b { font-weight: 700; }
  .contacts .mobile b { margin-right: 14px; }

  .back-field .person { left: 30px; top: 26px; }
  .web {
    position: absolute;
    font-weight: 700;
    font-size: 17px;
    line-height: 20px;
    color: var(--ink);
  }
  .back-field .web { left: 32px; top: 258px; }

  .back-plain .person { left: 30px; top: 44px; }
  .contact-grid {
    display: grid;
    grid-template-columns: 54px 1px auto;
    column-gap: 19px;
    margin-top: 20px;
    font-size: 15.5px;
    line-height: 20px;
  }
  .contact-grid .keys { text-align: right; font-weight: 700; }
  .contact-grid .rule { background: var(--rule); margin-top: -8px; height: 86px; }
  .back-plain .web { left: 32px; top: 249px; }
  .swoosh {
    position: absolute; left: 0; right: 0; bottom: 0; height: 70px;
  }
</style>
</head>
<body>
  <div class="side-label front">Side 1</div>
  <div class="side-label back">Side 2</div>

  <section class="card front">
    <div class="landscape" role="img" aria-label="Photo of a rural paddock with trees and hay bales under a blue sky"></div>
    <div class="brand-name">VODE MARKET<br>YARDS</div>
  </section>

  <section class="card back-field">
    <div class="faded-landscape" role="img" aria-label="Faded photo of a rural paddock with hay bales"></div>
    <div class="faint-name" aria-hidden="true">VODE<br>MARKET</div>
    <div class="person">
      <div class="name">Daniel Harlow</div>
      <div class="role">General Manager</div>
      <div class="contacts">
        <div><b>p:</b> (07) 3190 4826</div>
        <div class="mobile"><b>m:</b> +61 0491 7302</div>
        <div><b>e:</b> daniel.harlow@vodemarketyards.com.au</div>
      </div>
    </div>
    <div class="web">www.vodemarketyards.com.au</div>
  </section>

  <section class="card back-plain">
    <div class="faint-name" aria-hidden="true">VODE<br>MARKET</div>
    <div class="person">
      <div class="name">Daniel Harlow</div>
      <div class="role">General Manager</div>
      <div class="contact-grid">
        <div class="keys">phone<br>mobile<br>email</div>
        <div class="rule"></div>
        <div class="values">(07) 3190 4826<br>+61 0491 7302<br>daniel.harlow@vodemarketyards.com.au</div>
      </div>
    </div>
    <div class="web">www.vodemarketyards.com.au</div>
    <svg class="swoosh" viewBox="0 0 540 70" preserveAspectRatio="none" aria-hidden="true">
      <defs>
        <linearGradient id="swooshGrey" x1="0" y1="0" x2="0" y2="1">
          <stop offset="0" stop-color="#ffffff"/>
          <stop offset="1" stop-color="#e2e2e2"/>
        </linearGradient>
      </defs>
      <path d="M0 46 Q270 20 540 30 L540 48 L0 48 Z" fill="url(#swooshGrey)"/>
      <rect x="0" y="48" width="540" height="22" fill="var(--band)"/>
    </svg>
  </section>
</body>
</html>
```